Food Choices & Patient-Reported Outcomes in Parkinson's disease

We have spent the past 7 years studying food choices and rate of PD progression. We want to show people which foods have the most significant impact. <br/><br/>The infographic attached called "Kindred Living in QT" is the first in this 6-part series, recently designed by someone on PixelGuild. I'd like this entire series to "pair nicely" with one another, but also have unique personality, which is why I've opened the contest up. <br/><br/>The VEX-QT scale is the point of reference, it explains that higher scores are worse, low scores are better. I'd like to stick with the green is good, red is bad theme. ish. <br/><br/>The blue bar chart with food is "the grand finale." THIS is the information people have been waiting for for decades! I expect this to be highly circulated-- passed to physicians, support groups, getting tens of thousands of shares online! Below, I uploaded the 2019 version (also produced by someone from Pixel Guild). On my ppt screen shot, that data on the bottom left is also REALLY important. Can make another bar chart? Or find some other creative way to communicate it? OK to not include the p-values (OK to remove the far right column). Thanks!

Target Market(s)

Patients, their partners/ families, and health care providers.

Requirements
Must have
• Must include the legend-- some version of the VEX-QT scale vs. Quality of Life, as a point of reference. If possible, I'd like to stick with [some shade of] green is good, with it being clear that scores are getting worse [red-ish] as the scores increase.
• Must have the website, so people can go look for more information/ details about the project.
Nice to have
• Coordination with the "Kindred Living ..." infographic below.

```html
<!DOCTYPE html>
<html lang="en">
<head>
<meta charset="utf-8">
<title>Food Choices &amp; Parkinson Disease Progression</title>
<link href="https://fonts.googleapis.com/css2?family=Poppins:wght@400;500;600;700;800&display=swap" rel="stylesheet">
<style>
  :root{
    --cream:#fbf8d6;
    --orange:#f6913a;
    --yellow:#fccc3d;
    --teal:#4fc3b1;
    --teal-light:#9bd8cf;
    --ink:#4d4d4d;
    --peach:#fbe0c8;
    --white:#ffffff;
  }
  html,body{margin:0;padding:0;overflow:hidden;}
  body{width:1200px;height:728px;background:var(--white);font-family:"Poppins",sans-serif;position:relative;}
  .panel{position:absolute;display:block;}
  .panel svg{display:block;width:100%;height:100%;}
  svg text{font-family:"Poppins",sans-serif;}
  .progression{left:19.6px;top:27.2px;width:552.2px;height:324.2px;}
  .servings{left:571.8px;top:27.2px;width:301.4px;height:324.2px;}
  .cover{left:873.2px;top:27.2px;width:306.5px;height:324.2px;}
  .behaviors{left:19.6px;top:351.4px;width:552.2px;height:353.4px;}
  .scale{left:571.8px;top:351.4px;width:607.9px;height:353.4px;}
  .chart-title{font-weight:700;fill:var(--ink);}
  .axis-label{fill:var(--ink);font-weight:400;}
  .band-label{fill:var(--white);font-weight:700;}
  .food-name{fill:var(--white);font-weight:600;font-size:12px;}
  .food-good-val{fill:var(--teal);font-weight:600;font-size:12px;}
  .food-bad-val{fill:var(--orange);font-weight:600;font-size:12px;}
  .behavior{fill:var(--white);font-size:22px;}
  .score{fill:var(--white);font-weight:700;font-size:21px;}
  .score-bad{fill:var(--orange);font-weight:700;font-size:21px;}
  .band-note{font-weight:700;font-size:13px;}
  .band-note.warm{fill:var(--peach);}
  .band-note.cool{fill:var(--white);}
  .legend-label{fill:var(--ink);font-weight:500;font-size:18px;}
</style>
</head>
<body>

<!-- Progression by food-choice tier -->
<section class="panel progression">
  <svg viewBox="31 43 872 512">
    <rect x="31" y="43" width="872" height="512" fill="var(--cream)"/>
    <text class="chart-title" x="476" y="111" font-size="21" text-anchor="middle">Food Choices</text>
    <text class="chart-title" x="476" y="138" font-size="21" text-anchor="middle">And Parkinson’s Disease Progression</text>
    <g class="axis-label" font-size="17" text-anchor="end">
      <text x="172" y="180">2500</text><text x="172" y="233">2000</text>
      <text x="172" y="284">1500</text><text x="172" y="339">1000</text>
      <text x="168" y="389">500</text>
    </g>
    <text class="axis-label" font-size="17" transform="translate(101 290) rotate(-90)" text-anchor="middle">VEX-QT Measures</text>
    <polygon points="196,163 736,220 196,277" fill="var(--orange)"/>
    <polygon points="196,277 270,277 650,302 380,330 196,330" fill="var(--yellow)"/>
    <polygon points="196,330 340,330 573,356 375,383 196,383" fill="var(--teal-light)"/>
    <polygon points="196,383 260,383 393,410 290,437 196,437" fill="var(--teal)"/>
    <g class="band-label" font-size="21">
      <text x="208" y="228">POOR</text><text x="210" y="312">FAIR</text>
      <text x="208" y="364">GOOD</text><text x="208" y="418">EXCELENT</text>
    </g>
    <g class="axis-label" font-size="17" text-anchor="middle">
      <text x="196" y="476">0</text><text x="289" y="476">5</text><text x="382" y="476">10</text>
      <text x="475" y="476">15</text><text x="569" y="476">20</text><text x="663" y="476">25</text>
      <text x="757" y="476">30</text>
    </g>
    <text class="axis-label" x="463" y="515" font-size="18" text-anchor="middle">Years Since Diagnosis</text>
  </svg>
</section>

<!-- Servings per week impact -->
<section class="panel servings">
  <svg viewBox="903 43 476 512">
    <rect x="903" y="43" width="476" height="512" fill="var(--yellow)"/>
    <text class="chart-title" x="1141" y="96" font-size="22" text-anchor="middle">Impact of 2-4 Servings per Week on</text>
    <text class="chart-title" x="1141" y="122" font-size="22" text-anchor="middle">Parkinson Disease Severity</text>
    <g fill="var(--teal)">
      <rect x="1015" y="142" width="152" height="13"/>
      <rect x="1039" y="157" width="128" height="13"/>
      <rect x="1060" y="172" width="107" height="13"/>
      <rect x="1070" y="187" width="97" height="13"/>
      <rect x="1095" y="202" width="72" height="13"/>
      <rect x="1096" y="217" width="71" height="13"/>
      <rect x="1116" y="232" width="51" height="13"/>
      <rect x="1130" y="247" width="37" height="13"/>
    </g>
    <g text-anchor="end" class="food-good-val">
      <text x="1007" y="153">-225</text><text x="1031" y="168">-188</text><text x="1053" y="183">-161</text>
      <text x="1064" y="198">-144</text><text x="1087" y="213">-115</text><text x="1088" y="228">-114</text>
      <text x="1109" y="243">-79</text><text x="1123" y="258">-58</text>
    </g>
    <g class="food-name">
      <text x="1178" y="153">Fresh vegetable</text><text x="1178" y="168">Fresh fruits</text>
      <text x="1178" y="183">Nuts/seeds</text><text x="1178" y="198">Fish</text>
      <text x="1178" y="213">Wine</text><text x="1178" y="228">Olive oil</text>
      <text x="1178" y="243">Coconut oil</text><text x="1178" y="258">Fresh herb</text>
    </g>
    <g fill="var(--orange)">
      <rect x="1167" y="272" width="29" height="13"/><rect x="1167" y="287" width="35" height="13"/>
      <rect x="1167" y="302" width="38" height="13"/><rect x="1167" y="317" width="43" height="13"/>
      <rect x="1167" y="332" width="46" height="13"/><rect x="1167" y="347" width="46" height="13"/>
      <rect x="1167" y="362" width="47" height="13"/><rect x="1167" y="377" width="57" height="13"/>
      <rect x="1167" y="392" width="58" height="13"/><rect x="1167" y="407" width="72" height="13"/>
      <rect x="1167" y="422" width="75" height="13"/><rect x="1167" y="437" width="82" height="13"/>
      <rect x="1167" y="452" width="98" height="13"/><rect x="1167" y="467" width="99" height="13"/>
      <rect x="1167" y="482" width="133" height="13"/>
    </g>
    <g class="food-name" text-anchor="end">
      <text x="1154" y="283">Milk</text><text x="1154" y="298">Cheese</text><text x="1154" y="313">Yogurt</text>
      <text x="1154" y="328">Frozen vegetables</text><text x="1154" y="343">Pork</text><text x="1154" y="358">Chicken</text>
      <text x="1154" y="373">Plastic-bottled drink</text><text x="1154" y="388">Soda</text><text x="1154" y="403">Pasta</text>
      <text x="1154" y="418">Beef</text><text x="1154" y="433">Canned egg</text><text x="1154" y="448">Ice cream</text>
      <text x="1154" y="463">Fried food</text><text x="1154" y="478">Diet soda</text><text x="1154" y="493">Canned fruit</text>
    </g>
    <g class="food-bad-val">
      <text x="1204" y="283">42</text><text x="1209" y="298">51</text><text x="1211" y="313">56</text>
      <text x="1215" y="328">63</text><text x="1215" y="343">67</text><text x="1218" y="358">68</text>
      <text x="1219" y="373">69</text><text x="1228" y="388">84</text><text x="1231" y="403">86</text>
      <text x="1245" y="418">106</text><text x="1249" y="433">110</text><text x="1256" y="448">120</text>
      <text x="1272" y="463">144</text><text x="1276" y="478">146</text><text x="1307" y="493">191</text>
    </g>
  </svg>
</section>

<!-- Cover block -->
<section class="panel cover">
  <svg viewBox="1379 43 484 512">
    <rect x="1379" y="43" width="484" height="512" fill="var(--teal)"/>
    <text x="1432" y="96" font-size="30" font-weight="700" fill="var(--yellow)">2020</text>
    <g font-size="39" font-weight="800" fill="var(--yellow)">
      <text x="1432" y="266">Food Choices &amp;</text>
      <text x="1432" y="304">Parkinson Disease</text>
      <text x="1432" y="342">Progression</text>
    </g>
    <text x="1436" y="512" font-size="17" font-weight="700" fill="var(--white)">www.ThrivingDailyWithPD.org</text>
  </svg>
</section>

<!-- Dietary behaviours -->
<section class="panel behaviors">
  <svg viewBox="31 555 872 558">
    <rect x="31" y="555" width="872" height="558" fill="var(--orange)"/>
    <text class="chart-title" x="460" y="609" font-size="22" text-anchor="middle">Impact on Diatery Behaviors on PD Progression</text>
    <g class="behavior" text-anchor="end">
      <text x="568" y="656">I cook most of my meals</text>
      <text x="568" y="690">I avoid artificial sweeteners</text>
      <text x="568" y="724">I avoid soda</text>
      <text x="568" y="758">I avoid artificial colors, flavors</text>
      <text x="568" y="792">I routinely prepare meals for other</text>
      <text x="568" y="826">I avoid dairy</text>
      <text x="568" y="860">I eat organically grown foods when possible</text>
      <text x="568" y="894">I avoid pork</text>
      <text x="568" y="928">I buy from local farmers</text>
      <text x="568" y="962">I avoid beefs</text>
      <text x="568" y="996">I find it difficult to find healthy food</text>
      <text x="568" y="1030">It is difficult to afford groceries</text>
    </g>
    <g fill="var(--teal)">
      <rect x="656" y="635" width="72" height="27"/><rect x="668" y="669" width="72" height="27"/>
      <rect x="671" y="703" width="72" height="27"/><rect x="674" y="737" width="72" height="27"/>
      <rect x="676" y="771" width="72" height="27"/><rect x="680" y="805" width="72" height="27"/>
      <rect x="684" y="839" width="72" height="27"/><rect x="686" y="873" width="72" height="27"/>
      <rect x="688" y="907" width="72" height="27"/><rect x="691" y="941" width="72" height="27"/>
    </g>
    <g fill="var(--yellow)">
      <rect x="782" y="975" width="72" height="27"/><rect x="786" y="1009" width="72" height="27"/>
    </g>
    <g class="score" text-anchor="middle">
      <text x="692" y="657">-146</text><text x="704" y="691">-121</text><text x="707" y="725">-108</text>
      <text x="710" y="759">-106</text><text x="712" y="793">-105</text><text x="716" y="827">-92</text>
      <text x="720" y="861">-86</text><text x="722" y="895">-75</text><text x="724" y="929">-71</text>
      <text x="727" y="963">-63</text>
    </g>
    <g class="score-bad" text-anchor="middle">
      <text x="818" y="997">366</text><text x="822" y="1031">389</text>
    </g>
    <g stroke="var(--yellow)" stroke-width="2">
      <line x1="610" y1="1045" x2="860" y2="1045"/>
      <line x1="610" y1="1040" x2="610" y2="1050"/>
      <line x1="735" y1="1040" x2="735" y2="1050"/>
      <line x1="860" y1="1040" x2="860" y2="1050"/>
    </g>
    <text x="735" y="1068" font-size="12" font-weight="700" fill="var(--ink)" text-anchor="middle">Estimated impact on VEX-QT SCORE</text>
  </svg>
</section>

<!-- Scale legend -->
<section class="panel scale">
  <svg viewBox="903 555 960 558">
    <rect x="903" y="555" width="960" height="558" fill="var(--cream)"/>
    <text class="chart-title" x="1384" y="617" font-size="24" text-anchor="middle">Patients Reported Outcome in Parkinson’s Disease</text>
    <text class="chart-title" x="1384" y="647" font-size="22" text-anchor="middle">VEX-QT SCALE</text>
    <rect x="1069" y="675" width="631" height="129" fill="var(--orange)"/>
    <rect x="1069" y="804" width="631" height="59" fill="var(--yellow)"/>
    <rect x="1069" y="863" width="631" height="60" fill="var(--teal-light)"/>
    <rect x="1069" y="923" width="631" height="60" fill="var(--teal)"/>
    <g class="axis-label" font-size="19" text-anchor="end">
      <text x="1043" y="696">2500</text><text x="1043" y="755">2000</text><text x="1043" y="812">1500</text>
      <text x="1043" y="873">1000</text><text x="1039" y="930">500</text>
    </g>
    <text class="axis-label" font-size="18" transform="translate(964 817) rotate(-90)" text-anchor="middle">VEX-QT Measures</text>
    <g class="axis-label" font-size="19" text-anchor="middle">
      <text x="1071" y="1027">0</text><text x="1174" y="1027">5</text><text x="1279" y="1027">10</text>
      <text x="1384" y="1027">15</text><text x="1489" y="1027">20</text><text x="1594" y="1027">25</text>
    </g>
    <text class="axis-label" x="1370" y="1071" font-size="20" text-anchor="middle">Years Since Diagnosis</text>
    <g class="legend-label">
      <text x="1727" y="747">POOR</text><text x="1727" y="836">FAIR</text>
      <text x="1727" y="896">GOOD</text><text x="1727" y="955">EXCELENT</text>
    </g>
    <g fill="var(--peach)" opacity="0.9">
      <rect role="img" aria-label="Icon of a single person" x="1099" y="708" width="50" height="62" rx="10"/>
      <rect role="img" aria-label="Icon of fast food and a drink" x="1307" y="708" width="62" height="62" rx="8"/>
      <rect role="img" aria-label="Icon of a dumbbell" x="1515" y="710" width="60" height="60" rx="8"/>
    </g>
    <g fill="var(--white)" opacity="0.75">
      <rect role="img" aria-label="Icon of a group of friends" x="1093" y="900" width="60" height="40" rx="8"/>
      <rect role="img" aria-label="Icon of fresh fruit" x="1305" y="892" width="62" height="56" rx="8"/>
      <rect role="img" aria-label="Icon of a dumbbell" x="1515" y="893" width="60" height="58" rx="8"/>
    </g>
    <g class="band-note warm">
      <text x="1168" y="732">Overweight</text><text x="1168" y="750">Lonely</text>
      <text x="1382" y="714">Diary</text><text x="1382" y="732">Beef</text>
      <text x="1382" y="750">Chicken</text><text x="1382" y="768">Soda</text>
      <text x="1590" y="732">2 day / week</text><text x="1590" y="750">(No benefit)</text>
    </g>
    <g class="band-note cool">
      <text x="1168" y="907">A lot of friends</text><text x="1168" y="925">Eat organic</text><text x="1168" y="943">Cook own meal</text>
      <text x="1382" y="898">Fresh vegetables</text><text x="1382" y="916">Olive&amp;coconut oil</text>
      <text x="1382" y="934">Nut and seeds</text><text x="1382" y="952">Fresh fruits</text>
      <text x="1590" y="916">7 day / week</text><text x="1590" y="934">6 day / week</text>
    </g>
  </svg>
</section>

</body>
</html>
```